Consulting company with focus on aviation needs

We need a new business card design for our company. The company consults with multiple players in the industry like manufacturers and airlines. It is also a supplier and an inter-company level. Given the targeted industry (aviation) it should be both kind of serious, sound, secure, classy, ​​but also a bit technical, innovative. Should not be too playful, however, "fresh", "airy", "ligth" and "suprising" are suitabe attributes. The existing logo shall be used.

Airlines

```html
<!DOCTYPE html>
<html lang="en">
<head>
<meta charset="utf-8">
<title>Avelin – Business Card</title>
<link rel="stylesheet" href="https://fonts.googleapis.com/css2?family=Questrial&family=Montserrat:wght@600&display=swap">
<style>
  :root {
    --backdrop: #25272b;
    --card-dark: #221e1f;
    --teal: #22a387;
    --lime: #9cc05a;
    --slate: #6f7573;
    --orange: #f39a2b;
    --brand-grey: #8e9292;
    --white: #ffffff;
  }
  * { margin: 0; padding: 0; box-sizing: border-box; }
  html, body { width: 1200px; height: 1200px; overflow: hidden; }
  body {
    background: var(--backdrop);
    font-family: "Questrial", sans-serif;
    position: relative;
  }
  .card {
    position: absolute;
    left: 150px;
    width: 900px;
    height: 514px;
    background: var(--card-dark);
    overflow: hidden;
    box-shadow: 0 14px 40px rgba(0,0,0,.45);
  }
  .card--front { top: 44px; }
  .card--back { top: 642px; }

  .brand {
    position: absolute;
    display: flex;
    flex-direction: column;
    align-items: flex-start;
  }
  .card--front .brand { left: 50%; top: 50%; transform: translate(-50%, -50%); }
  .card--back .brand { left: 100px; top: 250px; }

  .brand__row { display: flex; align-items: center; gap: 20px; }
  .brand__dot {
    width: 58px; height: 58px; border-radius: 50%;
    background: var(--teal);
  }
  .brand__name {
    font-family: "Questrial", sans-serif;
    font-size: 64px;
    letter-spacing: 10px;
    color: var(--brand-grey);
    line-height: 1;
  }
  .brand__tagline {
    margin-top: 10px;
    margin-left: 78px;
    font-family: "Montserrat", sans-serif;
    font-weight: 600;
    font-size: 17px;
    letter-spacing: .5px;
    color: var(--orange);
  }

  .swoosh { position: absolute; inset: 0; width: 100%; height: 100%; }

  .contact {
    position: absolute;
    left: 600px;
    top: 96px;
    color: var(--white);
  }
  .contact__name {
    font-size: 30px;
    font-weight: 400;
    color: var(--lime);
    text-transform: uppercase;
    letter-spacing: .5px;
    line-height: 1.05;
  }
  .contact__role { font-size: 22px; margin-bottom: 34px; }
  .contact__address { font-size: 20px; line-height: 1.3; margin-bottom: 12px; }
  .contact__list { list-style: none; font-size: 20px; }
  .contact__item { display: flex; align-items: center; gap: 10px; height: 28px; }
  .contact__icon {
    width: 20px; height: 20px; border-radius: 50%;
    background: var(--lime);
    display: flex; align-items: center; justify-content: center;
    flex: none;
  }
  .contact__icon svg { width: 12px; height: 12px; }
</style>
</head>
<body>

<section class="card card--front">
  <div class="brand">
    <div class="brand__row">
      <span class="brand__dot"></span>
      <span class="brand__name">AVELIN</span>
    </div>
    <span class="brand__tagline">Linking Partners - Shaping Flight</span>
  </div>
</section>

<section class="card card--back">
  <svg class="swoosh" viewBox="0 0 900 514" preserveAspectRatio="none" aria-hidden="true">
    <path d="M175 0 L215 0 C360 50, 450 160, 495 260 C420 150, 320 50, 175 0 Z" fill="var(--slate)"/>
    <path d="M130 14 C290 40, 410 150, 470 255 C390 155, 280 60, 130 14 Z" fill="var(--lime)"/>
    <path d="M230 0 C400 50, 520 230, 600 514 L900 514 L900 0 Z" fill="var(--teal)"/>
  </svg>

  <div class="brand">
    <div class="brand__row">
      <span class="brand__dot"></span>
      <span class="brand__name">AVELIN</span>
    </div>
    <span class="brand__tagline">Linking Partners - Shaping Flight</span>
  </div>

  <div class="contact">
    <h1 class="contact__name">Mara Lindqvist</h1>
    <p class="contact__role">Manager</p>
    <p class="contact__address">418 Harbour Lane Suite 210<br>Oakridge ON K2M 4T6</p>
    <ul class="contact__list">
      <li class="contact__item">
        <span class="contact__icon"><svg viewBox="0 0 12 12"><rect x="3.5" y="1" width="5" height="10" rx="1" fill="none" stroke="#fff" stroke-width="1.2"/></svg></span>
        (555) 210 4480
      </li>
      <li class="contact__item">
        <span class="contact__icon"><svg viewBox="0 0 12 12"><path d="M3 1.5 L5 4 L4 5.2 C4.6 6.6 5.4 7.4 6.8 8 L8 7 L10.5 9 L9.2 10.5 C5.5 10 2 6.5 1.5 2.8 Z" fill="#fff"/></svg></span>
        (555) 210 4481
      </li>
      <li class="contact__item">
        <span class="contact__icon"><svg viewBox="0 0 12 12"><rect x="1.5" y="3" width="9" height="6.5" fill="none" stroke="#fff" stroke-width="1.2"/><path d="M1.5 3 L6 7 L10.5 3" fill="none" stroke="#fff" stroke-width="1.2"/></svg></span>
        info@avelin-consult.com
      </li>
      <li class="contact__item">
        <span class="contact__icon"><svg viewBox="0 0 12 12"><circle cx="6" cy="6" r="4.5" fill="none" stroke="#fff" stroke-width="1.1"/><path d="M1.5 6 H10.5 M6 1.5 C3.5 4 3.5 8 6 10.5 M6 1.5 C8.5 4 8.5 8 6 10.5" fill="none" stroke="#fff" stroke-width="1"/></svg></span>
        www.avelin-consult.com
      </li>
    </ul>
  </div>
</section>

</body>
</html>
```